help me Create Brightwell Catering offsite menus

I need something vibrant and it needs some pictures to go with the food i will include the logo of the location and the menu. it is for offsite catering to be delivered to venues in our local town, we are currently catering in house only but are expanding to do delivery so need something that i can use as a menu. the file needs to be able to be edited

Target Market(s)

local small businesses that require catering for their group lunches

Industry/Entity Type

Catering

Font styles to use
Serif
Decorative

Requirements
Must have
• colour and soul, must have a good feeling and be happy
Nice to have
• some other stock photos of the described products
Should not have
• not be too corporate and businessy

```html
<!DOCTYPE html>
<html lang="en">
<head>
<meta charset="utf-8">
<title>Brightwell Catering – Conference Menu</title>
<link rel="stylesheet" href="https://fonts.googleapis.com/css2?family=Barlow+Condensed:ital,wght@1,300;1,800&family=Questrial&display=swap">
<style>
  :root {
    --navy: #0b2538;
    --lime: #c9dc2a;
    --orange: #ee7623;
    --paper: #f2f2f4;
    --ink: #101820;
    --backdrop: #ffffff;
  }
  * { margin: 0; padding: 0; box-sizing: border-box; }
  html, body { width: 1100px; height: 1200px; overflow: hidden; background: var(--backdrop); }
  body { position: relative; font-family: "Questrial", "Century Gothic", sans-serif; color: var(--ink); }

  .menu-sheet { position: absolute; left: 217px; top: 70px; width: 751px; height: 1060px; background: var(--paper); }

  .brand-block { position: absolute; left: 22px; top: 21px; width: 158px; height: 144px; background: var(--navy);
    display: flex; align-items: center; justify-content: center; gap: 8px; }
  .brand-name { color: #fff; font-size: 21px; letter-spacing: 0.5px; }
  .brand-dot { width: 12px; height: 12px; border-radius: 50%; background: var(--lime); }

  .title-rule { position: absolute; left: 204px; width: 511px; height: 5px; }
  .title-rule--top { top: 52px; background: var(--lime); }
  .title-rule--bottom { top: 130px; background: var(--orange); }
  .menu-title { position: absolute; left: 204px; top: 58px; font-family: "Barlow Condensed", sans-serif; font-style: italic;
    font-size: 72px; line-height: 72px; color: var(--navy); white-space: nowrap; letter-spacing: 0.5px; }
  .menu-title strong { font-weight: 800; }
  .menu-title span { font-weight: 300; }

  .section-band { position: absolute; left: 39px; width: 712px; height: 59px; display: block; }
  .band-label { font-family: "Barlow Condensed", sans-serif; font-style: italic; font-weight: 800; font-size: 33px; fill: #fff; }
  .section-rule { position: absolute; left: 39px; width: 712px; height: 2px; }

  .item { position: absolute; left: 75px; font-size: 22px; letter-spacing: 0.4px; line-height: 1; white-space: nowrap; }
  .item-note { position: absolute; left: 79px; font-size: 14px; font-style: italic; color: var(--orange); line-height: 1; }
  .price { position: absolute; left: 548px; font-size: 19px; line-height: 1; white-space: nowrap; color: var(--navy); }
  .price small { font-size: 16px; }
</style>
</head>
<body>
<main class="menu-sheet">
  <div class="brand-block"><span class="brand-name">Brightwell</span><span class="brand-dot"></span></div>

  <div class="title-rule title-rule--top"></div>
  <h1 class="menu-title"><strong>CONFERENCE</strong> <span>MENU</span></h1>
  <div class="title-rule title-rule--bottom"></div>

  <!-- Tea & coffee -->
  <svg class="section-band" style="top:208px" viewBox="0 0 712 59">
    <defs><linearGradient id="teaPhoto" x1="0" x2="1"><stop offset="0" stop-color="#c9c6c2"/><stop offset=".5" stop-color="#a98a64"/><stop offset="1" stop-color="#6f5a44"/></linearGradient></defs>
    <polygon points="24,0 712,0 712,59 0,59" fill="url(#teaPhoto)" role="img" aria-label="Glass cups of tea on saucers"/>
    <polygon points="474,0 712,0 712,59 441,59" fill="var(--lime)"/>
    <text class="band-label" x="684" y="41" text-anchor="end">TEA &amp; COFFEE</text>
  </svg>
  <div class="section-rule" style="top:280px;background:var(--lime)"></div>

  <p class="item" style="top:298px">Tea and coffee station</p>
  <p class="item" style="top:343px">Continuous tea and coffee</p>
  <p class="item-note" style="top:367px">enough to serve for the day</p>
  <p class="item" style="top:388px">Barrista delivered</p>
  <p class="item-note" style="top:411px">pre order only</p>
  <p class="price" style="top:297px">$3.00 <small>pp</small></p>
  <p class="price" style="top:327px">$5.00 <small>pp</small></p>
  <p class="price" style="top:357px">$5.50 <small>each</small></p>

  <!-- Juice -->
  <svg class="section-band" style="top:451px" viewBox="0 0 712 59">
    <defs><linearGradient id="juicePhoto" x1="0" x2="1"><stop offset="0" stop-color="#e9e4e2"/><stop offset=".25" stop-color="#d9594a"/><stop offset=".6" stop-color="#c8361f"/><stop offset="1" stop-color="#e45a2a"/></linearGradient></defs>
    <polygon points="24,0 712,0 712,59 0,59" fill="url(#juicePhoto)" role="img" aria-label="Glass of tomato juice with fresh tomatoes"/>
    <polygon points="474,0 712,0 712,59 441,59" fill="var(--orange)"/>
    <text class="band-label" x="684" y="41" text-anchor="end">JUICE</text>
  </svg>
  <div class="section-rule" style="top:521px;background:var(--orange)"></div>

  <p class="item" style="top:536px">Juice 2 Lt Bottle</p>
  <p class="price" style="top:535px">$3.39</p>

  <!-- Morning or afternoon tea -->
  <svg class="section-band" style="top:583px" viewBox="0 0 712 59">
    <defs><linearGradient id="cupsPhoto" x1="0" x2="1"><stop offset="0" stop-color="#ece9e6"/><stop offset=".35" stop-color="#c9a988"/><stop offset=".6" stop-color="#8a4a3a"/><stop offset="1" stop-color="#e4ddd6"/></linearGradient></defs>
    <polygon points="24,0 712,0 712,59 0,59" fill="url(#cupsPhoto)" role="img" aria-label="White cups of tea, coffee and milk"/>
    <polygon points="329,0 712,0 712,59 297,59" fill="var(--lime)"/>
    <text class="band-label" x="686" y="38" text-anchor="end">Morning or Afternoon Tea</text>
  </svg>
  <div class="section-rule" style="top:653px;background:var(--orange)"></div>

  <p class="item" style="top:668px">Scones and Slice Platter</p>
  <p class="item" style="top:713px">Muffins</p>
  <p class="item" style="top:759px">Homemade biscuits</p>
  <p class="item" style="top:804px">Banana Bread</p>
  <p class="item" style="top:849px">Gluten Free Frittata</p>
  <p class="item" style="top:895px">Ploughmans Platter</p>
  <p class="item" style="top:940px">Whole Fresh Fruits Platter</p>
  <p class="item" style="top:986px">Chopped Fresh Seasonal Fruit Platter</p>

  <p class="price" style="top:667px">$6.50<small>per person</small></p>
  <p class="price" style="top:712px">$5.00<small>per person</small></p>
  <p class="price" style="top:757px">$4.50<small>per person</small></p>
  <p class="price" style="top:802px">$6.00<small>per person</small></p>
  <p class="price" style="top:848px">$5.50<small>per person</small></p>
  <p class="price" style="top:893px">$8.50<small>per person</small></p>
  <p class="price" style="top:938px">$45.00<small>per platter</small></p>
  <p class="price" style="top:984px">$49.50<small>per platter</small></p>
</main>
</body>
</html>
```